Need to have a client log in screen for work orders and estimate requests.
Nice informational landing page.

Stonefield is a full service general contractor servicing apartment complexes;
maintenance of grounds and apartments - remodeling and construction.

Design Specifics: We are pretty open here. Some good examples are
www.oakhavenworks.com , pellarestates.com and www.norvo7building.com

For the site we need:
Homepage - to explain services
Roofing page
Apartment Page
Client Portal - where clients can set up accounts to set up work/estimate request that will be routed to our email

--Will need coding, plan to host site on Wordpress

Target Market(s)

Multi family, Residential and commercial clients

Industry/Entity Type

Construction

Coding

Coded - Design and coding required

Number of Pages Required

3 page

Font styles to use
Serif

Requirements
Must have
• Client portal
Nice to have
• Not sure. please advise

```html
<!DOCTYPE html>
<html lang="en">
<head>
<meta charset="utf-8">
<title>Stonefield Construction</title>
<link href="https://fonts.googleapis.com/css2?family=Play:wght@400;700&family=Roboto+Condensed:wght@400;700&family=Open+Sans:wght@400;600&display=swap" rel="stylesheet">
<style>
:root{
  --ink:#111;
  --navy:#1b2288;
  --red:#c4161c;
  --dark:#1a1a1a;
  --grey-band:#ececec;
  --text:#444;
  --white:#fff;
}
*{margin:0;padding:0;box-sizing:border-box}
html,body{width:694px;height:1200px;overflow:hidden;background:var(--white)}
body{position:relative;font-family:"Open Sans",Arial,sans-serif;color:var(--text)}
.abs{position:absolute}
.topbar{left:0;top:0;width:694px;height:22px;background:#000;color:var(--white);font-size:7.5px}
.topbar .mail{left:82px;top:6px;display:flex;align-items:center;gap:6px}
.topbar .phone{right:82px;top:5px;display:flex;align-items:center;gap:5px;font-size:8.5px;font-weight:600}
.topbar .portal{right:170px;top:4px;height:14px;padding:0 8px;background:var(--red);color:var(--white);font-size:7.5px;font-weight:600;display:flex;align-items:center;gap:4px;border-radius:2px;text-decoration:none}
.nav{left:0;top:22px;width:694px;height:56px;background:var(--white)}
.nav a{position:absolute;top:22px;font-size:10px;color:var(--ink);text-decoration:none}
.nav .sep{position:absolute;top:22px;width:1px;height:13px;background:#ccc}
.brand{left:262px;top:10px;width:170px;height:40px;display:flex;align-items:center;justify-content:center;gap:6px;font-family:"Play",sans-serif;font-weight:700;font-size:20px;color:var(--ink);letter-spacing:1px}
.brand .mark{width:12px;height:12px;background:var(--red)}
.hero{left:0;top:78px;width:694px;height:276px;background:linear-gradient(180deg,#4f7fc0 0%,#9db8d8 22%,#c9a97a 45%,#a58257 75%,#6b5a44 100%)}
.hero .arrow{top:132px;width:16px;height:16px;background:#222;display:flex;align-items:center;justify-content:center}
.caption{left:0;top:232px;width:694px;height:44px;background:rgba(20,20,20,.72);color:var(--white);font-family:"Roboto Condensed",sans-serif;font-size:14.5px;line-height:17px;text-align:center;padding-top:5px}
.section-title{left:0;width:694px;text-align:center;font-family:"Play",sans-serif;font-weight:400;color:var(--navy);font-size:21.5px}
.divider{height:8px;display:flex;align-items:center;justify-content:center;gap:4px}
.divider i{display:block;border-top:1px dotted #888}
.divider b{display:block;width:7px;height:7px;background:var(--red);transform:rotate(45deg)}
.intro{left:83px;top:423px;width:528px;font-size:7.4px;line-height:12.8px;text-align:center;color:#555}
.btn{left:317px;top:483px;width:65px;height:19px;background:var(--red);color:var(--white);font-size:8.5px;font-weight:600;display:flex;align-items:center;justify-content:center;border-radius:2px}
.band{left:0;top:618px;width:694px;height:137px;background:var(--grey-band)}
.service{width:172px;text-align:center}
.service .icon{width:68px;height:68px;border-radius:50%;border:5px solid #ddd;margin:0 auto;display:flex;align-items:center;justify-content:center}
.service h3{font-family:"Roboto Condensed",sans-serif;font-weight:400;color:var(--navy);font-size:11px;margin-top:9px;white-space:nowrap}
.service p{font-family:Arial,sans-serif;font-size:7.2px;line-height:11px;color:#222;margin-top:6px}
.service .plus{width:11px;height:11px;background:#111;margin:6px auto 0;display:flex;align-items:center;justify-content:center}
.tile{position:absolute}
.tile.lead{left:78px;top:826px;width:196px;height:166px;background:linear-gradient(180deg,#3e5a30,#24331c)}
.tile.lead .over{position:absolute;left:0;right:0;top:54px;text-align:center;color:var(--white)}
.tile.lead h4{font-family:"Open Sans",sans-serif;font-size:10px;font-weight:600}
.tile.lead p{font-size:6.8px;line-height:12px;padding:3px 22px 0}
.gal-arrow{top:906px}
.footer{left:0;top:1016px;width:694px;height:156px;background:var(--dark);color:#ddd}
.footer h5{position:absolute;font-family:"Roboto Condensed",sans-serif;font-weight:400;font-size:10px;color:var(--white)}
.footer h5 span{color:var(--red)}
.footer .rule{position:absolute;height:1px;background:#333}
.footer .vline{position:absolute;width:1px;background:#333}
.links{position:absolute;left:82px;top:1066px;list-style:none;font-size:7.2px}
.links li{height:16px;display:flex;align-items:center;gap:8px}
.links li::before{content:"";width:3px;height:3px;border-radius:50%;background:var(--red)}
.contact-item{position:absolute;left:178px;display:flex;gap:10px;font-size:7px;line-height:10px}
.contact-item .ic{width:17px;height:17px;border-radius:50%;border:1px solid var(--red);display:flex;align-items:center;justify-content:center;flex:none}
.map{left:352px;top:1064px;width:258px;height:52px;background:linear-gradient(135deg,#eef0ea,#dfe5dc)}
.foot-brand{left:354px;top:1126px;display:flex;align-items:center;gap:8px;font-family:"Play",sans-serif;font-weight:700;font-size:19px;color:var(--white);letter-spacing:1px}
.foot-brand .mark{width:14px;height:14px;background:var(--red)}
.bottom{left:0;top:1172px;width:694px;height:28px;background:var(--red);color:var(--white);font-size:6.8px}
.bottom .copy{position:absolute;left:78px;top:10px}
.social{position:absolute;right:84px;top:7px;display:flex;gap:8px}
.social i{display:block;width:14px;height:14px;border-radius:50%;background:#3a66b5}
</style>
</head>
<body>
<div class="abs topbar">
  <div class="abs mail">
    <svg width="10" height="7" viewBox="0 0 10 7"><rect x=".5" y=".5" width="9" height="6" fill="none" stroke="#fff"/><path d="M.5 .5 5 4 9.5 .5" fill="none" stroke="#fff"/></svg>
    inquiry@stonefieldbuild.com
  </div>
  <a class="abs portal" href="#client-portal">
    <svg width="7" height="8" viewBox="0 0 7 8"><circle cx="3.5" cy="2" r="1.8" fill="#fff"/><path d="M0 8c0-2.5 1.5-3.5 3.5-3.5S7 5.5 7 8z" fill="#fff"/></svg>
    Client Portal Login
  </a>
  <div class="abs phone">
    <svg width="10" height="10" viewBox="0 0 10 10"><circle cx="5" cy="5" r="4.5" fill="none" stroke="#fff"/><path d="M3.5 2.8c0 2 1.5 4 3.5 4.4" fill="none" stroke="#fff" stroke-width="1.2"/></svg>
    555-014-2290
  </div>
</div>

<nav class="abs nav">
  <a style="left:83px">About Us</a><span class="sep" style="left:141px"></span>
  <a style="left:160px">Roofing</a>
  <div class="abs brand"><span class="mark"></span>STONEFIELD</div>
  <a style="left:481px">Apartment</a><span class="sep" style="left:545px"></span>
  <a style="left:566px">Contact Us</a>
</nav>

<div class="abs hero" role="img" aria-label="Photo of a two-storey apartment building under construction with wrapped walls and new roof framing">
  <div class="abs arrow" style="left:4px"><svg width="6" height="8"><path d="M5 1 1 4 5 7" fill="none" stroke="#fff" stroke-width="1.5"/></svg></div>
  <div class="abs arrow" style="right:4px"><svg width="6" height="8"><path d="M1 1 5 4 1 7" fill="none" stroke="#fff" stroke-width="1.5"/></svg></div>
  <div class="abs caption">Stonefield is a full service general contractor servicing apartment complexes,maintenance<br>of grounds and apartments - remodeling and construction.</div>
</div>

<h1 class="abs section-title" style="top:371px">Welcome to Stonefield Constructions</h1>
<div class="abs divider" style="left:187px;top:400px;width:320px"><i style="width:150px"></i><b></b><i style="width:150px"></i></div>
<p class="abs intro">Lorem ipsum dolor sit amet, consectetuer adipiscing elit, sed diam nonummy nibh euismod tincidunt ut laoreet dolore magna aliquam erat volutpat. Ut wisi enim ad minim veniam, quis nostrud exerci tation ullamcorper suscipit lobortis nisl ut aliquip ex ea commodo consequat. Duis autem vel eum iriure dolor in hendrerit in vulputate velit esse molestie consequat, vel illum dolore eu feugiat nulla facilisis at vero eros et accumsan et iusto odio dignissim qui blandit praesent luptatum zzril delenit augue duis dolore te feugait nulla facilisi.</p>
<div class="abs btn">Read More</div>

<h2 class="abs section-title" style="top:522px;letter-spacing:1px">OUR SERVICES</h2>
<div class="abs divider" style="left:280px;top:552px;width:134px"><i style="width:60px"></i><b></b><i style="width:60px"></i></div>

<div class="abs band"></div>
<div class="abs service" style="left:76px;top:584px">
  <div class="icon" style="background:var(--red)"><svg width="30" height="30" viewBox="0 0 30 30"><rect x="6" y="4" width="18" height="24" fill="#fff"/><g fill="var(--red)"><rect x="9" y="7" width="3" height="3"/><rect x="13.5" y="7" width="3" height="3"/><rect x="18" y="7" width="3" height="3"/><rect x="9" y="12" width="3" height="3"/><rect x="13.5" y="12" width="3" height="3"/><rect x="18" y="12" width="3" height="3"/><rect x="9" y="17" width="3" height="3"/><rect x="13.5" y="17" width="3" height="3"/><rect x="18" y="17" width="3" height="3"/><rect x="13" y="22" width="4" height="6"/></g></svg></div>
  <h3>Apartment Complexes</h3>
  <p>Lorem ipsum dolor sit amet, consectetuer adipiscing elit, sed diam nonummy nibh euismod tin laoreet volutpat.</p>
  <div class="plus"><svg width="7" height="7"><path d="M3.5 0v7M0 3.5h7" stroke="#fff" stroke-width="1.4"/></svg></div>
</div>
<div class="abs service" style="left:259px;top:584px">
  <div class="icon" style="background:#151515"><svg width="30" height="30" viewBox="0 0 30 30"><path d="M6 6l8 10" stroke="#fff" stroke-width="2"/><rect x="10" y="15" width="14" height="6" rx="1" fill="#fff"/><circle cx="12" cy="23" r="2.5" fill="#fff"/><circle cx="22" cy="23" r="2.5" fill="#fff"/></svg></div>
  <h3>Maintenance of Grounds &amp; Apartments</h3>
  <p>Lorem ipsum dolor sit amet, consectetuer adipiscing elit, sed diam nonummy nibh euismod tin laoreet volutpat.</p>
  <div class="plus"><svg width="7" height="7"><path d="M3.5 0v7M0 3.5h7" stroke="#fff" stroke-width="1.4"/></svg></div>
</div>
<div class="abs service" style="left:444px;top:584px">
  <div class="icon" style="background:var(--red)"><svg width="30" height="30" viewBox="0 0 30 30"><path d="M4 14l8-6 8 6v12H4z" fill="#fff"/><rect x="9" y="18" width="5" height="8" fill="var(--red)"/><path d="M19 8l7 7" stroke="#fff" stroke-width="2.5"/><rect x="21" y="4" width="7" height="4" fill="#fff" transform="rotate(45 24 6)"/></svg></div>
  <h3>Remodeling &amp; Construction</h3>
  <p>Lorem ipsum dolor sit amet, consectetuer adipiscing elit, sed diam nonummy nibh euismod tin laoreet volutpat.</p>
  <div class="plus"><svg width="7" height="7"><path d="M3.5 0v7M0 3.5h7" stroke="#fff" stroke-width="1.4"/></svg></div>
</div>

<h2 class="abs section-title" style="top:773px">Project Gallery</h2>
<div class="abs divider" style="left:280px;top:802px;width:134px"><i style="width:60px"></i><b></b><i style="width:60px"></i></div>

<svg class="abs gal-arrow" style="left:50px" width="12" height="20"><path d="M11 1 2 10l9 9" fill="none" stroke="#bbb" stroke-width="1.5"/></svg>
<svg class="abs gal-arrow" style="left:636px" width="12" height="20"><path d="M1 1l9 9-9 9" fill="none" stroke="#bbb" stroke-width="1.5"/></svg>

<div class="tile lead" role="img" aria-label="Photo of a tree-lined footpath through an apartment community">
  <div class="over"><h4>Lorem ipsum dolor</h4><p>Lorem ipsum dolor sit amet, consectetuer adipiscing elit, sed diam nonummy nibh euismod tincidunt ut laoreet dolore magna aliquam erat.</p></div>
</div>
<div class="tile" style="left:278px;top:826px;width:204px;height:76px;background:linear-gradient(180deg,#6d9be0 0%,#9e5a4a 45%,#7a8a8f 80%,#5d7a3e 100%)" role="img" aria-label="Photo of a modern multi-storey apartment block"></div>
<div class="tile" style="left:278px;top:908px;width:100px;height:84px;background:linear-gradient(180deg,#8fb2e0 0%,#b08a55 50%,#5a9a3a 100%)" role="img" aria-label="Photo of apartment buildings with a green lawn and walkway"></div>
<div class="tile" style="left:383px;top:908px;width:99px;height:84px;background:linear-gradient(180deg,#88ace0 0%,#b99066 55%,#8c6e4c 100%)" role="img" aria-label="Photo of a timber-framed house under construction"></div>
<div class="tile" style="left:487px;top:826px;width:132px;height:166px;background:linear-gradient(180deg,#c99a4f 0%,#b7853f 55%,#2a2a2a 75%,#c08d48 100%)" role="img" aria-label="Photo of a remodeled kitchen with wood cabinets and dark countertop"></div>

<footer class="abs footer">
  <h5 style="left:82px;top:20px">Quick <span>Links</span></h5>
  <div class="rule" style="left:82px;top:37px;width:70px"></div>
  <div class="vline" style="left:162px;top:20px;height:130px"></div>
  <h5 style="left:178px;top:21px">Contact <span>Details</span></h5>
  <div class="rule" style="left:178px;top:37px;width:145px"></div>
  <div class="vline" style="left:333px;top:20px;height:130px"></div>
  <h5 style="left:354px;top:20px">Location <span>Map</span></h5>
  <div class="rule" style="left:354px;top:37px;width:140px"></div>
</footer>
<ul class="links" style="color:#ddd">
  <li>Home</li><li>About Us</li><li>Roofing</li><li>Apartment</li><li>Contact Us</li>
</ul>
<div class="contact-item" style="top:1064px;color:#ddd">
  <span class="ic"><svg width="7" height="9" viewBox="0 0 7 9"><path d="M3.5 9S0 5 0 3.5a3.5 3.5 0 0 1 7 0C7 5 3.5 9 3.5 9z" fill="var(--red)"/><circle cx="3.5" cy="3.5" r="1.2" fill="#1a1a1a"/></svg></span>
  <span>Street Name City Name<br>State Zipcode</span>
</div>
<div class="contact-item" style="top:1095px;color:#ddd">
  <span class="ic"><svg width="8" height="8" viewBox="0 0 8 8"><path d="M1.5 1c0 3 2.5 5.5 5.5 5.5" fill="none" stroke="var(--red)" stroke-width="1.6"/></svg></span>
  <span>Phone<br><b style="font-weight:600;font-size:7.6px">555-014-2290</b></span>
</div>
<div class="contact-item" style="top:1126px;color:#ddd">
  <span class="ic"><svg width="9" height="6" viewBox="0 0 9 6"><rect x=".5" y=".5" width="8" height="5" fill="var(--red)"/><path d="M.5 .5 4.5 3.5 8.5 .5" fill="none" stroke="#1a1a1a" stroke-width=".8"/></svg></span>
  <span>Email<br>inquiry@stonefieldbuild.com</span>
</div>
<div class="abs map" role="img" aria-label="Street map showing the office location with two markers"></div>
<div class="abs foot-brand"><span class="mark"></span>STONEFIELD</div>

<div class="abs bottom">
  <span class="copy">Copyright © 2016 Stonefield Constructions . All Rights Reserved.</span>
  <div class="social"><i></i><i></i><i></i><i style="background:var(--white);opacity:.35"></i></div>
</div>
</body>
</html>
```